tax advisory service business cards
Professional
Loretta Fenwick
Tax Advisory Specialist
51924 HOLLISTER LANE SUITE C
MAPLECREST, LA 70812
FISCAL9COUNSELDESK@QUILLMAIL.COM
FCD4FILE.COM

```html
<!DOCTYPE html>
<html lang="en">
<head>
<meta charset="utf-8">
<title>Fiscal Counsel Desk — Business Cards</title>
<link href="https://fonts.googleapis.com/css2?family=Libre+Baskerville:wght@700&family=Open+Sans:ital,wght@0,400;0,600;1,400&display=swap" rel="stylesheet">
<style>
  :root {
    --backdrop: #e9e6e1;
    --card: #ffffff;
    --ink: #3a3a3a;
    --muted: #6b6b6b;
    --navy: #1f2d4d;
    --gold: #c9a23c;
    --accent: #e0a12a;
    --band: #141414;
  }
  * { margin: 0; padding: 0; box-sizing: border-box; }
  html, body { width: 1200px; height: 991px; overflow: hidden; }
  body {
    background: var(--backdrop);
    font-family: "Open Sans", sans-serif;
    color: var(--ink);
    position: relative;
  }
  .card {
    position: absolute;
    left: 250px;
    width: 700px;
    height: 400px;
    background: var(--card);
    box-shadow: 0 6px 18px rgba(0,0,0,0.18);
    overflow: hidden;
  }
  .card--back { top: 50px; }
  .card--front { top: 520px; }

  .brand-dot {
    flex: none;
    width: 44px; height: 44px; border-radius: 50%;
    background: var(--gold);
  }
  .brand-name {
    font-family: "Libre Baskerville", serif;
    font-weight: 700;
    font-size: 22px;
    color: var(--navy);
    letter-spacing: 1px;
    white-space: nowrap;
  }

  /* back */
  .brand-mark {
    position: absolute;
    left: 0; right: 0; top: 130px;
    display: flex; align-items: center; justify-content: center; gap: 14px;
  }
  .back-url {
    position: absolute; left: 0; right: 0; top: 232px;
    text-align: center;
    font-size: 13px; letter-spacing: 6px; color: var(--ink);
  }

  /* front */
  .front-brand {
    position: absolute; left: 36px; top: 96px; width: 300px;
  }
  .front-brand .brand-row { display: flex; align-items: center; gap: 10px; }
  .front-brand .brand-dot { width: 30px; height: 30px; }
  .front-brand .brand-name { font-size: 15px; letter-spacing: 0.5px; }
  .tagline {
    margin-top: 6px; font-size: 8.5px; color: var(--muted); font-style: italic;
    white-space: nowrap;
  }
  .front-url {
    position: absolute; left: 36px; top: 196px; width: 300px;
    font-size: 11px; letter-spacing: 5px; color: var(--ink);
  }
  .divider {
    position: absolute; left: 356px; top: 82px; width: 2px; height: 170px;
    background: var(--gold);
  }
  .contact { position: absolute; left: 378px; top: 82px; }
  .person-name { font-size: 17px; font-weight: 600; color: var(--accent); }
  .person-title { font-size: 12px; color: var(--muted); margin-bottom: 12px; }
  .contact-list { list-style: none; }
  .contact-list li {
    display: flex; align-items: flex-start; gap: 8px;
    font-size: 11px; line-height: 14px; margin-bottom: 5px; color: var(--ink);
    white-space: nowrap;
  }
  .contact-list svg { flex: none; width: 14px; height: 14px; }
  .band-wrap { position: absolute; left: 0; right: 0; top: 300px; }
  .band-line { height: 3px; background: var(--gold); }
  .band { height: 34px; background: var(--band); margin: 4px 0; }
</style>
</head>
<body>

<section class="card card--back" aria-label="Card back">
  <div class="brand-mark">
    <span class="brand-dot"></span>
    <span class="brand-name">FISCAL COUNSEL DESK, INC.</span>
  </div>
  <p class="back-url">www.FCD4FILE.com</p>
</section>

<section class="card card--front" aria-label="Card front">
  <div class="front-brand">
    <div class="brand-row">
      <span class="brand-dot"></span>
      <span class="brand-name">FISCAL COUNSEL DESK, INC.</span>
    </div>
    <p class="tagline">Your Partner in Small Business &amp; Personal Tax</p>
  </div>
  <p class="front-url">www.FCD4FILE.com</p>

  <div class="divider"></div>

  <div class="contact">
    <p class="person-name">Loretta Fenwick</p>
    <p class="person-title">Tax Advisory Specialist</p>
    <ul class="contact-list">
      <li>
        <svg viewBox="0 0 14 14"><circle cx="7" cy="7" r="7" fill="#c9a23c"/><path d="M7 3a2.5 2.5 0 0 0-2.5 2.5C4.5 7.5 7 11 7 11s2.5-3.5 2.5-5.5A2.5 2.5 0 0 0 7 3z" fill="#fff"/></svg>
        <span>51924 HOLLISTER LANE SUITE B<br>MAPLECREST, LA 70812</span>
      </li>
      <li>
        <svg viewBox="0 0 14 14"><circle cx="7" cy="7" r="7" fill="#c9a23c"/><path d="M4.5 3.5l1.5 0 .7 2-1 .8a5 5 0 0 0 2 2l.8-1 2 .7v1.5c0 .5-.5 1-1 1A6 6 0 0 1 3.5 4.5c0-.5.5-1 1-1z" fill="#fff"/></svg>
        <span>318-555-0148</span>
      </li>
      <li>
        <svg viewBox="0 0 14 14"><circle cx="7" cy="7" r="7" fill="#c9a23c"/><rect x="3.5" y="4.5" width="7" height="5" fill="#fff"/><path d="M3.5 4.5L7 7.3l3.5-2.8" stroke="#c9a23c" stroke-width=".8" fill="none"/></svg>
        <span>FISCAL9COUNSELDESK@QUILLMAIL.COM</span>
      </li>
      <li>
        <svg viewBox="0 0 14 14"><circle cx="7" cy="7" r="7" fill="#c9a23c"/><circle cx="7" cy="7" r="3.5" stroke="#fff" stroke-width=".9" fill="none"/><path d="M3.5 7h7M7 3.5c-1.5 2-1.5 5 0 7M7 3.5c1.5 2 1.5 5 0 7" stroke="#fff" stroke-width=".8" fill="none"/></svg>
        <span>www.FCD4FILE.COM</span>
      </li>
    </ul>
  </div>

  <div class="band-wrap">
    <div class="band-line"></div>
    <div class="band"></div>
    <div class="band-line"></div>
  </div>
</section>

</body>
</html>
```